Motivational Poster Design Project

I would like to create a poster with some of my favorite quotes to hang in my office.

Industry/Entity Type

Quotes

Requirements
Must have
• The poster will be 24" high x 36" long and printed on canvas, so the image you create needs to have a resolution of at least 2700 x 3900.

The poster must contain the following quotes:

“Your beliefs become your thoughts,
Your thoughts become your words,
Your words become your actions,
Your actions become your habits,
Your habits become your values,
Your values become your destiny.”
-Tavish Orlanno

"Winners practice until they get it right. Champions practice until they can’t get it wrong!"
-Unknown

"Style is the perfection of a point of view."
-Leopold Quimsby

"My interest in life comes from setting myself huge, apparently unachieveable challenges and trying to rise above them."
-Sir Edmund Valcourt

"Problems cannot be solved by the same level of thinking that created them."
-Bertram Holloway

"People think focus means saying yes to the thing you've got to focus on. But that's not what it means at all. It means saying no to the hundred other good ideas that there are. You have to pick carefully."
-Dale Morcum

"Think like a man of action and act like a man of thought."
-Lucien Fravel
Nice to have
• It would be nice to have an image of each person who is being quoted (if known) along with the quote that is attributable to them.

```html
<!DOCTYPE html>
<html lang="en">
<head>
<meta charset="utf-8">
<title>Quotes Poster</title>
<link href="https://fonts.googleapis.com/css2?family=Lora:wght@400&display=swap" rel="stylesheet">
<style>
  :root {
    --bg-black: #0b0b0b;
    --band-dark: #2c2c2c;
    --band-mid: #3d3d3d;
    --text-light: #dcdcdc;
    --portrait-light: #8a8a8a;
    --portrait-dark: #2a2a2a;
  }
  html, body {
    margin: 0;
    padding: 0;
    overflow: hidden;
    background: var(--bg-black);
  }
  .poster {
    position: relative;
    width: 831px;
    height: 1200px;
    overflow: hidden;
    background: var(--bg-black);
    font-family: "Lora", Georgia, serif;
    color: var(--text-light);
  }
  .band {
    position: absolute;
    left: 0;
    width: 831px;
    background:
      radial-gradient(ellipse at 60% 50%, var(--band-mid) 0%, var(--band-dark) 75%);
    overflow: hidden;
  }
  .portrait {
    position: absolute;
    top: 0;
    height: 100%;
  }
  .portrait--left {
    background: radial-gradient(ellipse at 50% 45%, var(--portrait-light) 0%, #555 40%, rgba(44,44,44,0) 75%);
  }
  .portrait--right {
    background: radial-gradient(ellipse at 50% 45%, var(--portrait-light) 0%, #555 40%, rgba(44,44,44,0) 75%);
  }
  .quote {
    position: absolute;
    margin: 0;
    text-align: center;
    font-size: 13.5px;
    line-height: 21px;
    letter-spacing: 2px;
  }
  .quote .attribution {
    display: block;
    margin-top: 12px;
    font-size: 14px;
    letter-spacing: 2.5px;
  }
  .closing {
    position: absolute;
    left: 0;
    top: 1080px;
    width: 831px;
    height: 120px;
    background: linear-gradient(#161616, #0e0e0e);
  }
  .closing .quote {
    left: 20px;
    width: 791px;
    top: 38px;
    font-size: 15px;
    line-height: 25px;
  }
</style>
</head>
<body>
<main class="poster">

  <section class="band" style="top:0;height:178px;">
    <div class="portrait portrait--left" style="left:40px;width:260px;" role="img" aria-label="Black and white portrait of Tavish Orlanno"></div>
    <blockquote class="quote" style="left:360px;width:420px;top:8px;line-height:19px;">
      “Your beliefs become your thoughts,<br>
      Your thoughts become your words,<br>
      Your words become your actions,<br>
      Your actions become your habits,<br>
      Your habits become your values,<br>
      Your values become your destiny.”
      <span class="attribution">- Tavish Orlanno</span>
    </blockquote>
  </section>

  <section class="band" style="top:186px;height:172px;">
    <div class="portrait portrait--right" style="left:540px;width:250px;" role="img" aria-label="Black and white portrait of Leopold Quimsby"></div>
    <blockquote class="quote" style="left:40px;width:380px;top:68px;">
      ”Style is the perfection of a point of view.”
      <span class="attribution">-Leopold Quimsby</span>
    </blockquote>
  </section>

  <section class="band" style="top:368px;height:172px;">
    <div class="portrait portrait--left" style="left:30px;width:290px;" role="img" aria-label="Black and white portrait of Bertram Holloway"></div>
    <blockquote class="quote" style="left:330px;width:480px;top:44px;">
      ”Problems cannot be solved by the same level of<br>thinking that created them.”
      <span class="attribution">- Bertram Holloway</span>
    </blockquote>
  </section>

  <section class="band" style="top:548px;height:170px;">
    <div class="portrait portrait--right" style="left:480px;width:290px;" role="img" aria-label="Black and white portrait of Edmund Valcourt"></div>
    <blockquote class="quote" style="left:40px;width:400px;top:24px;">
      ”My interest in life comes from setting<br>myself huge, apparently unachieveable<br>challenges and trying to rise above<br>them.”
      <span class="attribution">- Edmund Valcourt</span>
    </blockquote>
  </section>

  <section class="band" style="top:726px;height:172px;">
    <div class="portrait portrait--left" style="left:30px;width:260px;" role="img" aria-label="Black and white portrait of Dale Morcum"></div>
    <blockquote class="quote" style="left:290px;width:525px;top:26px;">
      ”People think focus means saying yes to the thing<br>you’ve got to focus on. But that’s not what it means at<br>all. It means saying no to the hundred other good<br>ideas that there are. You have to pick carefully.”
      <span class="attribution">- Dale Morcum</span>
    </blockquote>
  </section>

  <section class="band" style="top:906px;height:172px;">
    <div class="portrait portrait--right" style="left:510px;width:280px;" role="img" aria-label="Black and white portrait of Lucien Fravel"></div>
    <blockquote class="quote" style="left:40px;width:480px;top:52px;">
      ”Think like a man of action and act like a man of<br>thought.”
      <span class="attribution">- Lucien Fravel</span>
    </blockquote>
  </section>

  <section class="closing">
    <blockquote class="quote">
      ”Winners practice until they get it right. Champions practice until<br>they can’t get it wrong!” - Unknown
    </blockquote>
  </section>

</main>
</body>
</html>
```